Torvell Real Estate Management Consulting

To design a high end company profile that inspires confidence in high net worth individuals and similar clients. The profile to include real estate images, preferably real images. The firm is a Zambian firm and has its target to be comparable to Hoke & Company, Dunwarry & Company, Pellow Stroud, Old pell vasey pellow stroud, TLQA Real estate company as such.

Target Market(s)

Real estate clients such as high net worth individuals, private and public companies, government and international agencies, banks and insurance companies, trusts and pension funds and individual investors. the sub target market group being developers, planners, financiers, market analysts, designers, economists, engineers, architects, construction managers, quantity surveyors and public officials and others

Colors

Designer to choose colors to be used in the design.

Requirements
Must have
• Company logo

```html
<!DOCTYPE html>
<html lang="en">
<head>
<meta charset="utf-8">
<title>Torvell Real Estate – Company Profile Spread</title>
<link href="https://fonts.googleapis.com/css2?family=Lato:ital,wght@0,300;0,400;0,700;1,400&family=PT+Sans:wght@400;700&display=swap" rel="stylesheet">
<style>
  :root {
    --backdrop: #dcdcda;
    --navy: #3e4e95;
    --navy-light: #5b6cae;
    --grey-bar: #7d7d7d;
    --grey-cell: #8a8a8a;
    --paper: #ffffff;
    --ink: #2a2a2a;
    --muted-ink: #c8cde6;
  }
  * { margin: 0; padding: 0; box-sizing: border-box; }
  html, body { width: 1200px; height: 804px; overflow: hidden; background: var(--backdrop); }
  .spread { position: absolute; left: 40px; top: 40px; width: 1120px; height: 724px; display: flex; box-shadow: 0 6px 18px rgba(0,0,0,.18); }
  .page { position: relative; width: 560px; height: 724px; overflow: hidden; }

  /* Left page */
  .page--contents { background: radial-gradient(ellipse at 40% 20%, var(--navy-light) 0%, var(--navy) 60%); color: #fff; font-family: "Lato", sans-serif; }
  .contents__bar { position: absolute; left: 0; top: 292px; width: 140px; height: 26px; background: var(--grey-bar); }
  .contents__title { position: absolute; left: 148px; top: 284px; font-weight: 300; font-size: 27px; letter-spacing: -.3px; }
  .contents__list { position: absolute; left: 150px; top: 334px; list-style: none; font-size: 9.5px; line-height: 13.5px; }
  .contents__list li span { display: inline-block; width: 24px; }
  .contents__quote { position: absolute; left: 150px; top: 590px; width: 330px; font-style: italic; font-size: 13px; line-height: 18px; color: var(--muted-ink); }
  .contents__mark { position: absolute; left: 492px; top: 606px; font-family: "Lato", sans-serif; font-weight: 700; font-size: 52px; line-height: 1; color: var(--muted-ink); }
  .contents__rule { position: absolute; left: 150px; top: 672px; width: 78px; height: 3px; background: var(--muted-ink); }

  /* Right page */
  .page--profile { background: var(--paper); color: var(--ink); font-family: "PT Sans", sans-serif; }
  .profile__topline { position: absolute; left: 160px; top: 34px; width: 330px; height: 1px; background: var(--grey-bar); }
  .profile__tab { position: absolute; left: 488px; top: 24px; width: 72px; height: 18px; background: var(--navy); }
  .profile__tab-arrow { position: absolute; left: 494px; top: 27px; }
  .brand { position: absolute; left: 24px; top: 22px; display: flex; align-items: center; gap: 6px; }
  .brand__square { width: 14px; height: 14px; background: var(--navy); }
  .brand__name { font-family: "PT Sans", sans-serif; font-weight: 700; font-size: 11px; color: var(--navy); text-transform: uppercase; letter-spacing: .4px; }
  .profile__photo { position: absolute; left: 300px; top: 62px; width: 230px; height: 180px; background: linear-gradient(160deg, #2d5fa8 0%, #7fb3e3 45%, #d8ecfa 70%, #5c84b8 100%); }
  .profile__headline { position: absolute; left: 30px; top: 150px; font-family: "Lato", sans-serif; font-weight: 300; font-size: 28px; color: var(--navy); text-transform: uppercase; letter-spacing: -.5px; }
  .section-heading { position: absolute; left: 30px; font-weight: 700; font-size: 13px; color: var(--ink); }
  .section-heading--who { top: 194px; text-transform: uppercase; }
  .section-heading--solutions { top: 292px; }
  .body-copy { position: absolute; left: 30px; font-size: 9px; line-height: 11.5px; }
  .body-copy--who { top: 214px; width: 250px; }
  .body-copy--solutions { top: 312px; width: 500px; }
  .body-copy p + p { margin-top: 8px; }

  .services-table { position: absolute; left: 30px; top: 398px; width: 500px; border-collapse: collapse; font-size: 9px; line-height: 10.5px; }
  .services-table th { font-weight: 400; color: #fff; font-size: 10.5px; padding: 5px; }
  .services-table .col-core { width: 110px; background: var(--grey-cell); text-align: left; }
  .services-table .col-scope { background: var(--navy); }
  .services-table td { border: 1px solid #9a9a9a; padding: 6px 8px; vertical-align: top; }
  .services-table td.service-name { vertical-align: middle; }
  .services-table ul { list-style: none; }

  .profile__footer { position: absolute; left: 0; top: 676px; width: 560px; height: 48px; }
  .footer__grey { position: absolute; left: 0; top: 14px; width: 420px; height: 34px; background: var(--grey-bar); }
  .footer__page { position: absolute; left: 22px; top: 23px; width: 18px; height: 18px; border-radius: 50%; background: #fff; color: var(--navy); font-size: 10px; font-weight: 700; text-align: center; line-height: 18px; }
  .footer__contact { position: absolute; left: 110px; top: 27px; color: #fff; font-size: 8.5px; }
  .footer__blue { position: absolute; left: 420px; top: 0; width: 140px; height: 48px; background: var(--navy); border-left: 4px solid #fff; }
  .footer__social { position: absolute; left: 440px; top: 16px; display: flex; gap: 10px; }
  .footer__social span { width: 12px; height: 12px; background: #fff; }
</style>
</head>
<body>
<div class="spread">
  <section class="page page--contents">
    <div class="contents__bar"></div>
    <h2 class="contents__title">Content</h2>
    <ol class="contents__list">
      <li><span>03</span>WHO WE ARE</li>
      <li><span>04</span>SERVICES AND BUSINESS LINES</li>
      <li><span>05</span>INTEGRITY</li>
      <li><span>06</span>VISION</li>
      <li><span>07</span>ADD VALUE</li>
      <li><span>08</span>Uses Of Valuation Services</li>
      <li><span>09</span>OUR CLIENTS</li>
      <li><span>10</span>TEAMWORK</li>
    </ol>
    <p class="contents__quote">We assure our clients and prospective clients that our work is independent, objective and compliant with nationally recognized Laws of the Republic of Zambia.</p>
    <div class="contents__mark">”</div>
    <div class="contents__rule"></div>
  </section>

  <section class="page page--profile">
    <div class="profile__topline"></div>
    <div class="profile__tab"></div>
    <svg class="profile__tab-arrow" width="12" height="12" viewBox="0 0 12 12"><circle cx="6" cy="6" r="5.5" fill="#fff"/><path d="M7 3 L4 6 L7 9" stroke="#3e4e95" stroke-width="1.6" fill="none"/></svg>
    <div class="brand"><div class="brand__square"></div><div class="brand__name">Torvell Real Estate</div></div>
    <div class="profile__photo" role="img" aria-label="Photograph looking up at glass skyscrapers against a blue sky with clouds"></div>

    <h1 class="profile__headline">Inspire Value</h1>
    <h3 class="section-heading section-heading--who">Who We Are</h3>
    <div class="body-copy body-copy--who">
      <p>TRE | Management Consulting is one of Zambia's leading professional real estate services firms with an outstanding reputation and has its cornerstone the excellence of its people. Since its inception, the business has continued successfully with a national client base, a number of which have retained our services.</p>
    </div>
    <h3 class="section-heading section-heading--solutions">Our Solutions</h3>
    <div class="body-copy body-copy--solutions">
      <p>As a preferred property firm we continually monitor property value levels and will provide you with an update on market rents, trends and the position of your property in the marketplace. We continue to roll out our real estate services for you our clients to benefit from the power of our massive experience and database.</p>
      <p>Our system allows you to save on unnecessary research costs and time of doing new research in the marketplace and all due diligence is done when identifying the interests, benefits and rights being researched. We assure our clients and prospective clients that our work is independent, objective and compliant with nationally recognized Laws of the Republic of Zambia.</p>
    </div>

    <table class="services-table">
      <thead><tr><th class="col-core">Core Services</th><th class="col-scope">Scope</th></tr></thead>
      <tbody>
        <tr><td class="service-name">Consulting</td><td><ul>
          <li>Advisory Services</li><li>Acquisition, Leasing &amp; Disposal Advise</li><li>Business Plans</li><li>Feasibility studies</li><li>Highest and Best Use Studies</li><li>Market research/analysis</li><li>Planning and development</li><li>Property Condition Assessments</li></ul></td></tr>
        <tr><td class="service-name">Valuations</td><td><ul>
          <li>Agriculture Valuations</li><li>Asset Valuations</li><li>Commercial Valuations</li><li>Leisure/Hotels/Lodges</li><li>Industrial Valuations</li><li>Special purpose Valuations</li><li>Mines Valuations</li><li>Residential Valuations</li><li>Plant, Machinery &amp; Equipment</li></ul></td></tr>
        <tr><td class="service-name">Firm's Reference</td><td><ul>
          <li>The Kafue Property Appraisers Council</li><li>P.O Box 41186</li><li>Lusaka</li></ul></td></tr>
      </tbody>
    </table>

    <footer class="profile__footer">
      <div class="footer__grey"></div>
      <div class="footer__page">3</div>
      <div class="footer__contact">info@torvellpropertyadvisors.com | +260 955 418 206/ 0971 362584</div>
      <div class="footer__blue"></div>
      <div class="footer__social"><span></span><span></span><span></span><span></span></div>
    </footer>
  </section>
</div>
</body>
</html>
```